"loop-CAST." SoCal's Fishing Industry's single stop for the latest products, content, and services

Hi, looking for a website design for new LA based company called "loop-CAST." Where we showcase all the latest and greatest products, services, and content in a highly visually appealing platform for all fishing manufacturers and service providers as they relate to the fishing community (manufactures and service providers pay for cost-tiered content exposure and marketing, free exposure for manufacturers and service providers will have affiliate marketing link at minimal content exposure). As well, looking to include an in-site blog, store-products, and media content such as articles, video edits, and fishing condition picture galleries. Visually, looking for a minimalist/clean/blocked/ filterable and visually captivating gallery. Looking for a color pallet with white-background, deep blue- primary, light gray- secondary, light sky blue- third. Style- cleanliness and structure of widgetrove.example meets content like kpwildwater.example.

Target Market(s)

Primary- Southern California/Southwest Fishing Community, Secondary- All other US Fishing Communities

Coding

Coded - Design and coding required

Number of Pages Required

5+ page

Font styles to use
Sans Serif

Colors
959595
86cfc6
cadf82
333333
0555a3

Requirements
Must have
• Fast loading, mobile friendly, Analytics page, email sign up link for emailed newsletter (that is not a full page pop-up but integrated into browse bar), integrated social media links, search bar, filter link, home page return link, minimalist and clean design. Formatted to product showcase website style- please see attached files for ideas for design format and word-logo.
Should not have
• No Clutter, No background advertisements, No long text scripts outside of products main page,

```html
<!DOCTYPE html>
<html lang="en">
<head>
<meta charset="utf-8">
<title>loop-CAST. — Fishing Products, Content &amp; Services</title>
<link href="https://fonts.googleapis.com/css2?family=Poppins:wght@300;400;500;600;700;800&display=swap" rel="stylesheet">
<style>
:root{
  --blue:#0555a3;
  --blue-bar:#1a56a8;
  --blue-deep:#0a4a94;
  --leaf:#cadf82;
  --leaf-strong:#a9cf6b;
  --sky:#86cfc6;
  --grey:#959595;
  --ink:#333333;
  --line:#e4e4e4;
  --white:#ffffff;
}
*{box-sizing:border-box;margin:0;padding:0}
html,body{width:1200px;height:3197px;overflow:hidden}
body{position:relative;background:var(--white);font-family:'Poppins',sans-serif;color:var(--ink)}
.abs{position:absolute}

/* top bar */
.topbar{left:0;top:0;width:1200px;height:47px;background:var(--blue-bar);color:var(--white);font-size:11px;font-weight:500}
.topbar .item{position:absolute;top:0;height:47px;display:flex;align-items:center;gap:8px}
.topbar .sep{position:absolute;top:14px;width:1px;height:18px;background:rgba(255,255,255,.55)}
.social-dot{width:11px;height:11px;border:1.5px solid var(--white);border-radius:50%}

/* header */
.logo{left:86px;top:58px;font-size:38px;font-weight:800;color:#111;letter-spacing:-1px;line-height:1}
.menu-drop{left:86px;top:47px;width:181px;height:75px;background:var(--blue);color:var(--white);font-size:12px;padding:8px 0 0 22px;line-height:22px;border:1px solid #0a3f7c}
.browse{left:679px;top:63px;width:181px;height:41px;background:var(--blue);color:var(--white);font-size:12.5px;display:flex;align-items:center;padding-left:18px;gap:14px}
.browse .caret{position:absolute;right:10px;top:18px;border:4px solid transparent;border-top-color:var(--white)}
.search{left:860px;top:63px;width:257px;height:41px;border:1px solid #cfcfcf;font-size:12px;color:#a5a5a5;display:flex;align-items:center;padding-left:12px}
.search svg{position:absolute;right:16px;top:13px}
.browse-list{left:679px;top:104px;width:181px;height:127px;background:var(--blue);color:var(--white);font-size:12px;line-height:22px;padding:8px 0 0 22px;border:1px solid #0a3f7c;z-index:3}

/* hero */
.hero{top:120px;width:600px;height:461px}
.hero .caption{position:absolute;left:0;bottom:0;width:100%;height:67px;background:rgba(20,20,20,.55);color:var(--white);padding:10px 0 0 104px}
.hero-right .caption{padding-left:19px}
.caption h2{font-size:16.5px;font-weight:600;line-height:22px}
.caption p{font-size:10.5px;margin-top:4px}

/* intro */
.intro-title{left:0;top:602px;width:1200px;text-align:center;font-size:47px;font-weight:400;color:var(--blue);line-height:60px;letter-spacing:-.5px}
.intro-title span{color:var(--leaf);font-weight:600}
.intro-sub{left:0;top:656px;width:1200px;text-align:center;font-size:20px;letter-spacing:11px;color:var(--blue);font-weight:400;padding-left:11px}

/* shelves */
.shelf{left:86px;width:1027px;height:435px}
.shelf-head{position:absolute;left:0;top:0;width:100%;height:40px;border-bottom:1px solid var(--leaf)}
.shelf-head h3{position:absolute;left:0;top:4px;font-size:18.5px;font-weight:600;color:var(--blue)}
.pager{position:absolute;right:0;top:0;width:62px;height:30px;border:1px solid #ddd;display:flex;align-items:center;justify-content:center;gap:12px}
.cards{position:absolute;left:0;top:71px;width:100%;display:flex;gap:26px}
.card{width:237px;height:360px;border:1px solid var(--line);position:relative;background:var(--white)}
.card .photo{height:227px}
.card h4{position:absolute;top:238px;left:0;width:100%;text-align:center;font-size:14.5px;font-weight:500;line-height:20px;color:var(--blue)}
.card .rule{position:absolute;left:10px;top:300px;width:216px;height:1px;background:#777}
.card .rule::after{content:"";position:absolute;left:98px;top:-1px;width:22px;height:3px;background:var(--sky)}
.tag{position:absolute;top:318px;height:31px;font-size:12px;display:flex;align-items:center;justify-content:center}
.tag.on{left:9px;width:105px;background:var(--leaf-strong);color:var(--white)}
.tag.off{left:120px;width:107px;border:1px solid #cfcfcf;color:var(--grey)}

/* brands */
.brand-row{left:86px;top:2319px;width:1027px;height:80px}
.brand-nav{position:absolute;top:0;width:29px;height:80px;background:var(--blue);display:flex;align-items:center;justify-content:center}
.brand-tile{position:absolute;top:0;width:125px;height:80px;border-left:1px solid #cfcfcf;border-right:1px solid #cfcfcf;display:flex;align-items:center;justify-content:center}
.brand-tile i{display:block;width:58px;height:58px;border-radius:50%;background:#dcdcdc}

/* contact */
.contact{left:0;top:2489px;width:1200px;height:375px;background:linear-gradient(120deg,#2866b6 0%,#1b57a6 55%,#164e9b 100%)}
.contact h3{position:absolute;left:86px;top:64px;font-size:18.5px;font-weight:600;color:var(--white)}
.contact .rule{position:absolute;left:86px;top:101px;width:1027px;height:1px;background:rgba(255,255,255,.7)}
.field{position:absolute;height:40px;border:1px solid rgba(255,255,255,.85);color:var(--white);font-size:12.5px;padding:10px 15px}
.submit{position:absolute;left:86px;top:273px;width:1027px;height:31px;background:var(--white);color:var(--ink);font-size:12px;text-align:center;line-height:31px}

/* footer */
.footer{left:0;top:2864px;width:1200px;height:333px;background:var(--ink);color:#bdbdbd}
.fcol{position:absolute;top:64px}
.fcol h5{font-size:18.5px;font-weight:600;color:var(--white);margin-bottom:16px}
.fcol p{font-size:11px;line-height:22px}
.ficons{display:flex;gap:18px;margin:-2px 0 14px;align-items:center}
.ficons span{width:12px;height:12px;border:1.5px solid #bdbdbd;border-radius:50%}
.ficons span:first-child{border-color:var(--sky)}
.copyright{position:absolute;left:0;top:289px;width:1200px;text-align:center;font-size:11px;color:#bdbdbd}
</style>
</head>
<body>

<!-- top bar -->
<div class="abs topbar">
  <div class="item" style="left:86px">MORE
    <svg width="9" height="6" viewBox="0 0 9 6"><path d="M0 0h9L4.5 6z" fill="#fff"/></svg>
  </div>
  <div class="sep" style="left:164px"></div>
  <div class="item" style="left:181px">OUR BLOG</div>
  <div class="sep" style="left:744px"></div>
  <div class="item" style="left:765px;gap:13px"><span class="social-dot"></span><span class="social-dot"></span><span class="social-dot"></span></div>
  <div class="sep" style="left:853px"></div>
  <div class="item" style="left:874px;gap:10px">
    <svg width="15" height="13" viewBox="0 0 15 13"><path d="M0 6 15 0 12 13 7 9 12 3 5 8z" fill="#fff"/></svg>
    REGISTER FOR NEWSLETTER
  </div>
  <div class="sep" style="left:1063px"></div>
  <div class="item" style="left:1083px">
    <svg width="12" height="12" viewBox="0 0 12 12"><path d="M2.5 0 4.5 3 3 4.5C4 6.8 5.2 8 7.5 9L9 7.5 12 9.5 10.5 12C4.5 11.5.5 7.5 0 1.5z" fill="#fff"/></svg>
  </div>
</div>

<!-- header -->
<div class="abs logo">loop-CAST.</div>
<div class="abs menu-drop">About<br>List Your Product<br>Other</div>
<div class="abs browse">
  <svg width="18" height="14" viewBox="0 0 18 14" fill="#fff"><rect x="0" y="0" width="3" height="2.5"/><rect x="5" y="0" width="13" height="2.5"/><rect x="0" y="5.7" width="3" height="2.5"/><rect x="5" y="5.7" width="13" height="2.5"/><rect x="0" y="11.5" width="3" height="2.5"/><rect x="5" y="11.5" width="13" height="2.5"/></svg>
  Browse Button<span class="caret"></span>
</div>
<div class="abs search">Search products...
  <svg width="14" height="14" viewBox="0 0 14 14"><circle cx="6" cy="6" r="4.5" fill="none" stroke="#222" stroke-width="2"/><path d="M9.3 9.3 13 13" stroke="#222" stroke-width="2.2"/></svg>
</div>
<div class="abs browse-list">Trading<br>Featured<br>Staff Picks<br>Offstore<br>Trading</div>

<!-- hero -->
<div class="abs hero" style="left:0;background:radial-gradient(circle at 45% 70%,#4f5b2a 0%,#3d3524 40%,#1f1a14 100%)" role="img" aria-label="Fishing rod and reel with green line and lures on a wooden table">
  <div class="caption"><h2>LOREM IPSUM IS SIMPLY DUMMY TEXT PRINTING</h2><p>by Ray Hollis | 21 Dec 2017</p></div>
</div>
<div class="abs hero hero-right" style="left:600px;background:linear-gradient(180deg,#6f8a3e 0%,#8fa76a 30%,#c7d0cf 55%,#9fb0b8 80%,#7d8f98 100%)" role="img" aria-label="Two anglers fly fishing in a river">
  <div class="caption"><h2>LOREM IPSUM IS SIMPLY DUMMY TEXT PRINTING</h2><p>by Ray Hollis | 21 Dec 2017</p></div>
</div>

<!-- intro -->
<h1 class="abs intro-title">LOREM IPSUM <span>LOREM IPSUM</span></h1>
<p class="abs intro-sub">LOREM IPSUM SIMPLY DUMMY TEXT INDUSTRY.</p>

<!-- shelf template pager svg used inline -->
<section class="abs shelf" style="top:748px">
  <div class="shelf-head"><h3>FEATURED CONTENT</h3>
    <div class="pager">
      <svg width="13" height="12" viewBox="0 0 13 12"><path d="M6 0 0 6l6 6M0 6h13" fill="none" stroke="#a9cf6b" stroke-width="2.4"/></svg>
      <svg width="13" height="12" viewBox="0 0 13 12"><path d="M7 0l6 6-6 6M13 6H0" fill="none" stroke="#222" stroke-width="2.4"/></svg>
    </div>
  </div>
  <div class="cards">
    <article class="card"><div class="photo" role="img" aria-label="Fishing reel and rod against a blue sky" style="background:linear-gradient(160deg,#5c9ad6,#2f6db3 60%,#c9c3a5)"></div><h4>Aenean Ru Bristique printing<br>and typesetting</h4><div class="rule"></div><span class="tag on">#Lorem ipsum</span><span class="tag off">#Lorem Ipsum</span></article>
    <article class="card"><div class="photo" role="img" aria-label="Angler holding a large pike on a lake" style="background:linear-gradient(170deg,#b9cdd3,#7f9a7a 55%,#3f5a38)"></div><h4>Aenean Ru Bristique printing<br>and typesetting</h4><div class="rule"></div><span class="tag on">#Lorem ipsum</span><span class="tag off">#Lorem Ipsum</span></article>
    <article class="card"><div class="photo" role="img" aria-label="Tuna landed in a net in deep blue water" style="background:radial-gradient(circle at 55% 40%,#3a78b8,#0f3d7c 70%)"></div><h4>Aenean Ru Bristique printing<br>and typesetting</h4><div class="rule"></div><span class="tag on">#Lorem ipsum</span><span class="tag off">#Lorem Ipsum</span></article>
    <article class="card"><div class="photo" role="img" aria-label="Fish farm pens in a mountain bay" style="background:linear-gradient(180deg,#c4cfd8,#8ea0ad 35%,#3e6c86 60%,#2f5f7c)"></div><h4>Aenean Ru Bristique printing<br>and typesetting</h4><div class="rule"></div><span class="tag on">#Lorem ipsum</span><span class="tag off">#Lorem Ipsum</span></article>
  </div>
</section>

<section class="abs shelf" style="top:1250px">
  <div class="shelf-head"><h3>TRENDING CONTENT</h3>
    <div class="pager">
      <svg width="13" height="12" viewBox="0 0 13 12"><path d="M6 0 0 6l6 6M0 6h13" fill="none" stroke="#a9cf6b" stroke-width="2.4"/></svg>
      <svg width="13" height="12" viewBox="0 0 13 12"><path d="M7 0l6 6-6 6M13 6H0" fill="none" stroke="#222" stroke-width="2.4"/></svg>
    </div>
  </div>
  <div class="cards" style="top:72px">
    <article class="card"><div class="photo" role="img" aria-label="Angler on a boat holding a large silver fish" style="background:linear-gradient(180deg,#8db7e0,#3f78b6 45%,#a7a9ab 70%,#d9d3c6)"></div><h4>Aenean Ru Bristique printing<br>and typesetting</h4><div class="rule"></div><span class="tag on">#Lorem ipsum</span><span class="tag off">#Lorem Ipsum</span></article>
    <article class="card"><div class="photo" role="img" aria-label="Fishing boats moored in a harbour" style="background:linear-gradient(180deg,#7288a4,#9aa9bb 50%,#3b5878 75%,#2a4563)"></div><h4>Aenean Ru Bristique printing<br>and typesetting</h4><div class="rule"></div><span class="tag on">#Lorem ipsum</span><span class="tag off">#Lorem Ipsum</span></article>
    <article class="card"><div class="photo" role="img" aria-label="Canoe on a lake at sunset among reeds" style="background:linear-gradient(180deg,#29362e,#c9a45c 35%,#6f6a43 60%,#1e2b1e)"></div><h4>Aenean Ru Bristique printing<br>and typesetting</h4><div class="rule"></div><span class="tag on">#Lorem ipsum</span><span class="tag off">#Lorem Ipsum</span></article>
    <article class="card"><div class="photo" role="img" aria-label="Coiled ropes on a wooden pier" style="background:linear-gradient(170deg,#9bb2bf,#6d6255 40%,#4b4035)"></div><h4>Aenean Ru Bristique printing<br>and typesetting</h4><div class="rule"></div><span class="tag on">#Lorem ipsum</span><span class="tag off">#Lorem Ipsum</span></article>
  </div>
</section>

<section class="abs shelf" style="top:1752px">
  <div class="shelf-head"><h3>NEW STUFF</h3>
    <div class="pager">
      <svg width="13" height="12" viewBox="0 0 13 12"><path d="M6 0 0 6l6 6M0 6h13" fill="none" stroke="#a9cf6b" stroke-width="2.4"/></svg>
      <svg width="13" height="12" viewBox="0 0 13 12"><path d="M7 0l6 6-6 6M13 6H0" fill="none" stroke="#222" stroke-width="2.4"/></svg>
    </div>
  </div>
  <div class="cards">
    <article class="card"><div class="photo" role="img" aria-label="Fish, reels and lures on a white board" style="background:linear-gradient(160deg,#eeeeec,#b7b9b2 55%,#7c8074)"></div><h4>Aenean Ru Bristique printing<br>and typesetting</h4><div class="rule"></div><span class="tag on">#Lorem ipsum</span><span class="tag off">#Lorem Ipsum</span></article>
    <article class="card"><div class="photo" role="img" aria-label="Fishing lures on weathered planks" style="background:linear-gradient(180deg,#6e6862,#8a837a 50%,#5c5650)"></div><h4>Aenean Ru Bristique printing<br>and typesetting</h4><div class="rule"></div><span class="tag on">#Lorem ipsum</span><span class="tag off">#Lorem Ipsum</span></article>
    <article class="card"><div class="photo" role="img" aria-label="Binoculars, compass and reel" style="background:linear-gradient(150deg,#2a2a2a,#6a6a66 40%,#e8e8e6 75%)"></div><h4>Aenean Ru Bristique printing<br>and typesetting</h4><div class="rule"></div><span class="tag on">#Lorem ipsum</span><span class="tag off">#Lorem Ipsum</span></article>
    <article class="card"><div class="photo" role="img" aria-label="Spinning reel on rope and net" style="background:linear-gradient(160deg,#cdb88c,#8a7350 50%,#e2dccb)"></div><h4>Aenean Ru Bristique printing<br>and typesetting</h4><div class="rule"></div><span class="tag on">#Lorem ipsum</span><span class="tag off">#Lorem Ipsum</span></article>
  </div>
</section>

<!-- brands -->
<section class="abs shelf" style="top:2244px;height:40px">
  <div class="shelf-head"><h3>BRAND</h3></div>
</section>
<div class="abs brand-row">
  <div class="brand-nav" style="left:0"><svg width="6" height="10" viewBox="0 0 6 10"><path d="M5 1 1 5l4 4" fill="none" stroke="#fff" stroke-width="1.5"/></svg></div>
  <div class="brand-tile" style="left:68px" role="img" aria-label="Partner brand mark"><i></i></div>
  <div class="brand-tile" style="left:221px" role="img" aria-label="Partner brand mark"><i></i></div>
  <div class="brand-tile" style="left:375px" role="img" aria-label="Partner brand mark"><i></i></div>
  <div class="brand-tile" style="left:528px" role="img" aria-label="Partner brand mark"><i></i></div>
  <div class="brand-tile" style="left:682px" role="img" aria-label="Partner brand mark"><i></i></div>
  <div class="brand-tile" style="left:835px" role="img" aria-label="Partner brand mark"><i></i></div>
  <div class="brand-nav" style="left:998px"><svg width="6" height="10" viewBox="0 0 6 10"><path d="M1 1l4 4-4 4" fill="none" stroke="#fff" stroke-width="1.5"/></svg></div>
</div>

<!-- contact -->
<section class="abs contact">
  <h3>CONTACT</h3>
  <div class="rule"></div>
  <div class="field" style="left:86px;top:133px;width:237px">Name</div>
  <div class="field" style="left:350px;top:133px;width:235px">Phone No</div>
  <div class="field" style="left:613px;top:133px;width:236px">Email</div>
  <div class="field" style="left:877px;top:133px;width:236px">Subject</div>
  <div class="field" style="left:86px;top:183px;width:1027px;height:77px">Comment</div>
  <div class="submit">Submit</div>
</section>

<!-- footer -->
<footer class="abs footer">
  <div class="fcol" style="left:86px;width:230px"><h5>ABOUT US</h5>
    <p>Lorem Ipsum is simply dummy text of the printing and typesetting industry. Lorem Ipsum is simply dummy text of the printing and typesetting industry.</p></div>
  <div class="fcol" style="left:350px"><h5>PRODUCT LINK</h5>
    <p>Lorem IpsumLorem Ipsum<br>Lorem IpsumLorem Ipsum<br>Lorem IpsumLorem Ipsum<br>Lorem IpsumLorem Ipsum</p></div>
  <div class="fcol" style="left:613px"><h5>OTHER</h5>
    <p>Specials<br>New Products<br>Best Sellers<br>Our Stores</p></div>
  <div class="fcol" style="left:877px"><h5>SOCIAL MEDIA</h5>
    <div class="ficons"><span></span><span></span><span></span><span></span><span></span><span></span></div>
    <p style="line-height:26px">Lorem IpsumLorem Ipsum<br>Lorem IpsumLorem Ipsum</p></div>
  <p class="copyright">©Copyright 2018 loop-CAST.com. | All Rights Reserved</p>
</footer>

</body>
</html>
```